Health Coaching Brochure for Healthcare Practioners

I am looking to have a tri-fold brochure created marketed towards healthcare practitioners (doctors, nurses, surgeons, etc), to get them to purchase 1-on-1 health coaching from me.
I've provided the text/content (in pdf & pages), my logo, a picture of me, and two color palettes, but please also include lots of white space. I would like to design to be very clean, modern & crisp. Also include additional photos, of doctors, etc taking care of themselves & feeling happy (maybe eating healthy, maybe exercising, feeling good & happy!)
Please also see http://brightoakwellness.com and http://instagram.com/brightoakwellness for a feel of my brand.
Thank you!
Target Market(s)
Healthcare Practioners (mainly based in Los Angeles, for now)
Industry/Entity Type
Healthcare
Look and feel

```html
<!DOCTYPE html>
<html lang="en">
<head>
<meta charset="UTF-8">
<title>Bright Oak Wellness – Tri-fold Brochure</title>
<link href="https://fonts.googleapis.com/css2?family=Cabin+Sketch:wght@700&family=Patua+One&family=Open+Sans:ital,wght@0,300;0,400;0,700;1,400;1,700&display=swap" rel="stylesheet">
<style>
:root{
  --navy:#1c4469;
  --navy-deep:#183d60;
  --sky:#6cb6e4;
  --sky-soft:#7dc0ea;
  --teal:#2fa2b8;
  --gold:#f2b705;
  --white:#ffffff;
  --paper:#f7f7f7;
  --ink:#111111;
  --brand-blue:#1b78c4;
  --canvas:#c9c9c9;
}
*{box-sizing:border-box;margin:0;padding:0}
html,body{width:1200px;height:1200px;overflow:hidden;background:var(--canvas)}
body{position:relative;font-family:"Open Sans",sans-serif}
.spread{position:absolute;left:190px;width:820px;height:562px;display:flex;box-shadow:0 2px 8px rgba(0,0,0,.18)}
.spread--outside{top:24px}
.spread--inside{top:614px}
.panel{position:relative;width:273.33px;height:100%;overflow:hidden}
.photo{position:absolute;display:block}

/* outside: headline panel */
.headline-panel{background:var(--white)}
.headline-block{position:absolute;left:0;top:0;width:100%;height:390px;background:var(--navy);text-align:center;padding-top:40px;font-family:"Cabin Sketch",sans-serif;font-weight:700;line-height:.95}
.headline-block .gold{color:var(--gold)}
.headline-block .white{color:var(--white)}
.hl-1{font-size:31px;text-align:left;padding-left:24px}
.hl-2{font-size:38px;text-align:left;padding-left:24px}
.hl-3{font-size:40px;text-align:left;padding-left:24px}
.hl-4{font-size:30px;margin-top:6px}
.hl-5{font-size:31px;margin-top:6px}
.hl-6{font-size:29px;margin-top:6px}
.hl-7{font-size:33px;margin-top:8px}
.headline-photo{left:40px;top:390px;width:200px;height:172px;background:linear-gradient(180deg,#eef0f3,#d9dde2)}

/* outside: bio panel */
.bio-panel{background:var(--sky)}
.bio-photo{left:32px;top:12px;width:210px;height:275px;background:linear-gradient(160deg,#b8b5b0,#8e8a85)}
.bio-text{position:absolute;left:16px;right:14px;top:300px;color:#a9d5f2;font-size:10.6px;line-height:13.8px;font-weight:300}
.bio-text p{text-align:justify;margin-bottom:13px}
.bio-text strong{font-weight:700;font-style:italic}

/* outside: cover */
.cover-panel{background:var(--white)}
.brand-name{position:absolute;left:0;right:0;top:215px;text-align:center;font-family:"Open Sans",sans-serif;font-weight:700;font-size:19px;color:var(--ink)}
.cover-offer{position:absolute;left:0;right:0;top:250px;text-align:center;font-family:"Patua One",serif;color:var(--brand-blue)}
.cover-offer .big{font-size:44px;line-height:1.1}
.cover-offer .sub{font-size:23px;line-height:1.05}

/* inside: services */
.services-panel{background:var(--teal);color:var(--white);padding:62px 8px 0 22px}
.services-title{font-weight:700;font-style:italic;font-size:11px;line-height:13.5px;text-transform:uppercase;padding-right:24px}
.services-copy{font-size:10.6px;line-height:13.5px;margin-top:14px;padding-right:40px}
.services-sub{font-weight:700;font-style:italic;font-size:10.6px;line-height:16px;margin-top:24px}
.service-list{list-style:none;margin-top:1px}
.service-list li{font-size:10.4px;line-height:16.8px;position:relative;padding-left:26px;white-space:nowrap}
.service-list li::before{content:"";position:absolute;left:5px;top:5px;width:7px;height:7px;background:var(--white)}
.services-note{position:absolute;left:0;right:0;top:436px;text-align:center;font-weight:700;font-style:italic;font-size:10.6px;line-height:14px}
.access{position:absolute;left:26px;top:492px;font-family:"Patua One",serif;font-size:20px;line-height:23px}

/* inside: commitment */
.commit-panel{background:var(--white)}
.commit-block{position:absolute;left:0;top:0;width:100%;height:372px;background:var(--navy-deep);color:var(--white);padding:28px 18px 0 18px}
.commit-title{font-family:"Patua One",serif;font-size:16px;line-height:18px;font-weight:400}
.commit-sub{font-size:10.5px;line-height:13px;margin-top:4px}
.notes-card{position:absolute;left:20px;top:98px;width:232px;height:198px;background:var(--paper)}
.notes-card svg{display:block}
.commit-cta{position:absolute;left:16px;right:60px;top:306px}
.commit-cta .commit-title{font-size:16.5px;line-height:18px}
.commit-cta .commit-sub{margin-top:2px;white-space:nowrap}
.commit-photo{left:60px;top:382px;width:160px;height:172px;background:linear-gradient(180deg,#f0f1f3,#dcdfe3)}

/* inside: story + testimonials */
.story-panel{background:var(--sky-soft);color:var(--white);padding:52px 28px 0 44px}
.story-panel p{font-style:italic;font-size:12.3px;line-height:16.4px;margin-bottom:14px}
.testimonials-title{font-size:14px;font-weight:400;letter-spacing:.3px;margin-top:26px}
.testimonial{position:absolute;left:46px;width:200px;height:76px}
.testimonial--one{top:388px}
.testimonial--two{top:482px}
.testimonial q{position:absolute;left:0;top:0;width:112px;font-style:italic;font-size:6.6px;line-height:9px}
.testimonial .t-photo{left:132px;top:0;width:50px;height:52px;background:linear-gradient(160deg,#9eb3c4,#5d6f7e)}
.testimonial .t-name{position:absolute;left:132px;top:54px;width:50px;text-align:center;font-size:6.5px}
.testimonial .t-place{position:absolute;left:126px;top:64px;width:62px;text-align:center;font-size:4.6px;font-style:italic}
</style>
</head>
<body>

<section class="spread spread--outside">
  <div class="panel headline-panel">
    <div class="headline-block">
      <div class="hl-1 gold">CHANGE THE</div>
      <div class="hl-2 gold">WAY</div>
      <div class="hl-3 gold">YOU LIVE</div>
      <div class="hl-4 white">GET IN SHAPE</div>
      <div class="hl-5 gold">LOSE WEIGHT</div>
      <div class="hl-6 white">TONE UP</div>
      <div class="hl-7 gold">LOOK &amp;<br>FEEL BETTER<br>THAN EVER</div>
    </div>
    <div class="photo headline-photo" role="img" aria-label="Photo of a doctor in a white coat and tie lifting a dumbbell"></div>
  </div>

  <div class="panel bio-panel">
    <div class="photo bio-photo" role="img" aria-label="Portrait photo of the health coach smiling against a grey wall"></div>
    <div class="bio-text">
      <p><strong>Elena Marlowe</strong> is a holistic health coach, personal trainer, and fitness nutritionist who empowers healthcare practitioners who are exhausted and overwhelmed to find uncomplicated ways to minimize their stress and to make themselves and their health a priority.</p>
      <p>It's time to take care of YOU. You deserve it!<br>Are you ready for a change? Let's talk! Schedule your complimentary 15-minute consultation to discuss your unique situation and your goals. Visit brightoakwellness.com, email elena@brightoakwellness or call Elena at 555.014.2290.</p>
    </div>
  </div>

  <div class="panel cover-panel">
    <div class="brand-name">bright oak wellness</div>
    <div class="cover-offer">
      <div class="big">1-on-1</div>
      <div class="sub">personal training<br>los angeles, CA</div>
    </div>
  </div>
</section>

<section class="spread spread--inside">
  <div class="panel services-panel">
    <h2 class="services-title">Get the most out of your workout by working out with a personl trainer</h2>
    <p class="services-copy">Customized workout program, from beginnier to advanced</p>
    <p class="services-copy">Provide motivation, support, and accountability</p>
    <p class="services-sub">Achieve your fitness goals<br>and have fun doing it</p>
    <ul class="service-list">
      <li>Fat Loss</li>
      <li>Weight Training</li>
      <li>Cardiovascular Training</li>
      <li>Muscular Development &amp; Toning</li>
      <li>Sports Performance Training</li>
      <li>Body Composition Analysis</li>
      <li>Specialized Diet Plans</li>
      <li>Nutrition &amp; Supplementation Counseling</li>
      <li>Wedding Preparation</li>
    </ul>
    <p class="services-note">Integrative Nutrition &amp;<br>Health Coaching available, as well.</p>
    <p class="access">+24-hour<br>access to trainer</p>
  </div>

  <div class="panel commit-panel">
    <div class="commit-block">
      <h2 class="commit-title">function movements!</h2>
      <p class="commit-sub">based on how your body was designed to move</p>
      <div class="notes-card">
        <svg width="232" height="198" viewBox="0 0 232 198" aria-hidden="true">
          <g stroke="#a9cde0" stroke-width="0.8">
            <line x1="14" y1="24" x2="218" y2="24"/>
            <line x1="14" y1="50" x2="218" y2="50"/>
            <line x1="14" y1="76" x2="218" y2="76"/>
            <line x1="14" y1="102" x2="218" y2="102"/>
            <line x1="14" y1="128" x2="218" y2="128"/>
            <line x1="14" y1="154" x2="218" y2="154"/>
            <line x1="14" y1="180" x2="218" y2="180"/>
          </g>
        </svg>
      </div>
      <div class="commit-cta">
        <h2 class="commit-title">ready to make the commitment?</h2>
        <p class="commit-sub">schedule your 15 minute consultation today!</p>
      </div>
    </div>
    <div class="photo commit-photo" role="img" aria-label="Photo of a female doctor with a stethoscope shrugging"></div>
  </div>

  <div class="panel story-panel">
    <p>Helping others is my passion. Seeing the change in someone throughout their fitness journey is incredible. Not just physically, but also emotionally. They have become more confident, more optimistic, healthier and stronger in all aspects of their life.</p>
    <p>Working with all different skill sets and fitness levels I am always working for my clients. Doing everything I can to teach them how to live a healthier life. let's do it together!</p>
    <h3 class="testimonials-title">TESTIMONIALS</h3>
    <div class="testimonial testimonial--one">
      <q>Lorem ipsum dolor sit amet, consectetur adipiscing elit, sed do eiusmod tecommodo consequat. Duis aute iaecat cupidatat non proident, sunt in culpa qui officia deserunt mollit anim id est laborum.</q>
      <div class="photo t-photo" role="img" aria-label="Photo of a smiling client couple"></div>
      <div class="t-name">NAME</div>
      <div class="t-place">Biltmore, Phoenix, AZ</div>
    </div>
    <div class="testimonial testimonial--two">
      <q>Lorem ipsum dolor sit amet, consectetur adipiscing elit, sed do eiusmod tecommodo consequat. Duis aute iaecat cupidatat non proident, sunt in culpa qui officia deserunt mollit anim id est laborum.</q>
      <div class="photo t-photo" role="img" aria-label="Photo of a client couple dressed up"></div>
      <div class="t-name">NAME</div>
      <div class="t-place">Biltmore, Phoenix, AZ</div>
    </div>
  </div>
</section>

</body>
</html>
```